Corporate marketing website with signup form

The function of the website is to promote our 2 product offerings. It will contain a main screen and several 5-7 sub-pages that will be available as 'scroll down' anchors and as front-page navigation links on the top of the page.

Navigation menu labels are: Products, Unique Model, Pricing, About, and Contact

Target Market(s)

Business to business marketers who are looking to source lead generation services

Industry/Entity Type

Marketing

Logo Text

VelQuora

Coding

Coded - Design and coding required

Number of Pages Required

5+ page

Requirements
Must have
• A sign-up form on main section of the front page. Fields are First Name, Last Name, Company, and Email (all text), and a pull-down with three options (only pick one): Track 1, Track 2, Custom Combination.
• Also incorporate the bottom half (ie crop the image) of the EPS file attached (the 'blue heads). Add this to the lower portion of the main screen and have the rest of the blue background become the background for the next anchored section of the navigation.
• You'll see the main section text in the mock-up I provided. The rest of the menu items/anchors can be lorem ipsum for now.
• Can this be coded in Wordpress? That would be my preference so I can edit it in the future.

```html
<!DOCTYPE html>
<html lang="en">
<head>
<meta charset="utf-8">
<title>VelQuora – List and Audience Building</title>
<link rel="stylesheet" href="https://fonts.googleapis.com/css2?family=Open+Sans:ital,wght@0,300;0,400;0,600;0,700;1,400&family=Arimo:ital,wght@0,400;0,700;1,700&display=swap">
<style>
:root{
  --navy:#0d2a47;
  --navy-deep:#08203a;
  --sky:#6ec8e6;
  --sky-dark:#4fb3d8;
  --blue:#0f8fd6;
  --btn-blue:#0d6aa8;
  --ink:#1f2a36;
  --grey-text:#444;
  --tab:#4a4a4a;
  --beige:#ebe7e1;
  --orange:#e2a27c;
  --steel:#d0dae0;
  --charcoal:#2f3039;
  --white:#fff;
}
*{box-sizing:border-box;margin:0;padding:0}
html,body{width:1200px;height:3803px;overflow:hidden}
body{font-family:'Open Sans',sans-serif;color:var(--ink);background:var(--white);position:relative}
.abs{position:absolute}

/* nav */
.site-nav{position:absolute;top:0;left:0;width:1200px;height:76px;background:var(--white)}
.brand{position:absolute;left:177px;top:16px;font-family:'Arimo',sans-serif;font-size:36px;color:var(--navy-deep)}
.menu{position:absolute;left:522px;top:0;display:flex;height:60px;font-family:'Arimo',sans-serif;font-size:17px}
.menu a{display:flex;align-items:center;padding:0 20px;color:var(--navy-deep);text-decoration:none}
.menu a.active{background:var(--sky);color:var(--white)}

/* hero */
.hero{position:absolute;top:76px;left:0;width:1200px;height:578px;background:radial-gradient(ellipse at 75% 70%,#17375a 0%,var(--navy) 50%,var(--navy-deep) 100%)}
.hero h1{position:absolute;left:177px;top:138px;width:440px;font-family:'Arimo',sans-serif;font-weight:700;font-size:28px;line-height:36px;color:var(--white)}
.hero .lede{position:absolute;left:177px;width:420px;font-family:'Arimo',sans-serif;font-style:italic;font-weight:700;font-size:14px;line-height:18px;color:var(--white)}
.phone-box{position:absolute;left:177px;top:342px;width:383px;height:64px;border:2px solid var(--white);display:flex;align-items:center;color:var(--white)}
.phone-box .ico{width:56px;height:100%;border-right:2px solid var(--white);display:flex;align-items:center;justify-content:center}
.phone-box span{font-size:30px;letter-spacing:2px;padding-left:24px}

.signup{position:absolute;left:641px;top:36px;width:381px;height:484px;background:var(--white);border-radius:4px;box-shadow:0 20px 40px rgba(0,0,0,.35);text-align:center}
.signup h2{font-size:23px;font-weight:600;margin-top:20px}
.social-login{display:flex;justify-content:center;margin-top:14px}
.social-login span{height:50px;line-height:50px;color:var(--white);font-size:20px;font-weight:600}
.social-login .left{width:148px;background:#3b5b96;border-radius:25px 0 0 25px;text-align:right;padding-right:18px}
.social-login .right{width:148px;background:#1ba1e6;border-radius:0 25px 25px 0;text-align:left;padding-left:18px}
.or{display:flex;align-items:center;justify-content:center;gap:14px;margin-top:10px;color:#5a8fbd;font-style:italic;font-size:18px}
.or i{display:block;width:110px;height:2px;background:#c4d4e4}
.signup h3{font-size:23px;font-weight:600;margin-top:4px}
.fields{margin:18px 24px 0;display:grid;grid-template-columns:1fr 1fr;gap:22px 22px}
.field{height:32px;border:1px solid #c8ccd0;border-radius:3px;font-size:12px;color:#888;text-align:left;padding:7px 10px;position:relative}
.field.full{grid-column:1/3}
.field .caret{position:absolute;right:0;top:0;width:26px;height:30px;border-left:1px solid #c8ccd0;display:flex;align-items:center;justify-content:center}
.signup .btn{display:inline-block;margin-top:28px;width:132px;height:40px;line-height:40px;background:#4a4a4a;color:var(--white);border-radius:4px;font-size:17px;font-weight:600}
.signup .member{font-size:10px;margin-top:18px;color:#333}
.signup .member b{font-weight:700}

/* banner strip */
.strip{position:absolute;top:654px;left:0;width:1200px;height:61px;background:linear-gradient(#6ec8e6,#5dbde0)}

/* tracks */
.tracks{position:absolute;top:715px;left:0;width:1200px;height:438px;background:var(--sky)}
.track{position:absolute;top:45px;width:381px;height:355px;background:var(--white)}
.track .tab{position:absolute;left:-20px;top:0;height:50px;width:186px}
.track .tab svg{position:absolute;left:0;top:0}
.track .tab span{position:absolute;left:50px;top:7px;color:var(--white);font-family:'Arimo',sans-serif;font-size:28px}
.track .body{position:absolute;left:20px;top:80px;width:345px;font-family:'Arimo',sans-serif;font-size:13.5px;line-height:18px;color:#333}
.track .body h4{font-size:14.5px;font-weight:700;margin-bottom:6px;line-height:18px}

/* unique model */
.section-title{position:absolute;left:0;width:1200px;text-align:center;font-weight:400;font-size:44px;color:var(--ink)}
.model-sub{position:absolute;top:1228px;left:0;width:1200px;text-align:center;font-family:'Arimo',sans-serif;font-weight:700;font-size:18px;color:#333}
.diamond{position:absolute;width:222px;height:222px;background:var(--beige);transform:rotate(45deg)}
.diamond .inner{position:absolute;left:-20px;top:40px;width:262px;transform:rotate(-45deg);transform-origin:131px 71px;text-align:center}
.diamond h5{font-size:16px;font-weight:700;margin-bottom:8px}
.diamond p{font-size:11.5px;line-height:16px;color:#333;padding:0 14px}
.diamond.active{background:var(--blue);color:var(--white);box-shadow:0 0 0 1px var(--blue)}
.diamond.active p{color:var(--white)}

/* pricing */
.pricing{position:absolute;top:1863px;left:0;width:1200px;height:703px;background:linear-gradient(180deg,#1f3856 0%,#33475e 35%,#3d3733 70%,#1c1c1f 100%)}
.pricing .section-title{top:30px;color:var(--white)}
.plan{position:absolute;background:var(--steel);text-align:center;box-shadow:0 10px 24px rgba(0,0,0,.45)}
.plan .label{background:#dfe4e7;font-size:14px;color:#333;display:flex;align-items:center;justify-content:center}
.plan .price{background:var(--orange);color:var(--white)}
.plan .price b{display:block;font-weight:400;font-size:58px;line-height:1}
.plan .price small{font-size:20px}
.plan ul{list-style:none;padding:18px 22px 0;text-align:left}
.plan li{font-size:12.5px;color:#333;border-bottom:1px solid #a9b4bb;padding:10px 0 9px}
.plan li:last-child{border-bottom:none}
.plan .cta{position:absolute;left:0;bottom:0;width:100%;background:#4b4b4d;color:var(--white);font-size:21px;display:flex;align-items:center;justify-content:center}

/* about */
.about h2{position:absolute;left:177px;top:2614px;font-weight:400;font-size:44px}
.about .lead{position:absolute;left:177px;top:2690px;width:500px;font-family:'Arimo',sans-serif;font-weight:700;font-size:14.5px}
.about .text{position:absolute;left:177px;top:2720px;width:500px;font-family:'Arimo',sans-serif;font-size:15px;line-height:19px;color:#444}
.about .photo{position:absolute;left:702px;top:2647px;width:322px;height:248px;background:linear-gradient(135deg,#d6dde3 0%,#6f7f90 45%,#2b3440 100%)}
.btn-read{position:absolute;left:177px;top:2903px;width:173px;height:43px;background:var(--btn-blue);color:var(--white);font-size:19px;display:flex;align-items:center;justify-content:center}

/* contact */
.contact{position:absolute;top:3017px;left:0;width:1200px;height:385px;background:var(--sky)}
.contact h2{position:absolute;top:28px;left:0;width:1200px;text-align:center;color:var(--white);font-weight:400;font-size:44px}
.contact .sub{position:absolute;top:88px;left:0;width:1200px;text-align:center;color:var(--white);font-style:italic;font-size:22px}
.cfield{position:absolute;left:330px;width:266px;height:38px;background:var(--white);border:1px solid #4a6f86;font-size:11px;padding:10px 8px;color:#333}
.cfield svg{position:absolute;right:8px;top:12px}
.cmsg{position:absolute;left:603px;top:167px;width:269px;height:127px;background:var(--white);border:1px solid #4a6f86;font-size:11px;padding:8px;color:#333}
.cmsg svg{position:absolute;right:8px;top:8px}
.btn-submit{position:absolute;left:535px;top:317px;width:132px;height:36px;border-radius:18px;background:var(--btn-blue);color:var(--white);font-size:17px;display:flex;align-items:center;justify-content:center}

/* call bar */
.callbar{position:absolute;top:3402px;left:0;width:1200px;height:96px;background:var(--charcoal);color:var(--white)}
.callbar .msg{position:absolute;left:290px;top:36px;font-weight:700;font-size:18px;letter-spacing:.5px}
.callbar .num{position:absolute;left:730px;top:28px;font-weight:700;font-size:30px;letter-spacing:1px}

/* get in touch */
.touch{position:absolute;top:3498px;left:0;width:1200px;height:249px;background:var(--sky);color:var(--white);text-align:center}
.touch h2{font-weight:400;font-size:30px;margin-top:24px}
.touch p{font-size:13.5px;line-height:22px;margin-top:8px}
.social-row{position:absolute;top:150px;left:0;width:1200px;display:flex;justify-content:center;align-items:center}
.social-row .dot{width:24px;height:24px;border-radius:50%;background:var(--white)}
.social-row .line{width:60px;height:1px;background:rgba(255,255,255,.8);margin:0 26px}
.copyright{position:absolute;top:3747px;left:0;width:1200px;height:56px;text-align:center;line-height:56px;font-size:13px;color:#666}
</style>
</head>
<body>

<header class="site-nav">
  <div class="brand">VelQuora</div>
  <nav class="menu">
    <a class="active" href="#products">Products</a>
    <a href="#model">Unique Model</a>
    <a href="#pricing">Pricing</a>
    <a href="#about">About</a>
    <a href="#contact">Contact</a>
  </nav>
</header>

<section class="hero" id="home">
  <h1>List and Audience Building for your Content Marketing Efforts</h1>
  <p class="lede" style="top:226px">Lorem Ipsum is simply dummy text of the printing and typesetting industry. Lorem Ipsum has been the industry's standard dummy text</p>
  <p class="lede" style="top:300px">Lorem Ipsum is simply dummy text of the printing</p>
  <div class="phone-box">
    <div class="ico">
      <svg width="34" height="34" viewBox="0 0 24 24" fill="none" stroke="#fff" stroke-width="1.8"><path d="M5 3h4l2 5-2.5 1.5a11 11 0 0 0 6 6L16 13l5 2v4a2 2 0 0 1-2 2A16 16 0 0 1 3 5a2 2 0 0 1 2-2z"/><path d="M15 3a6 6 0 0 1 6 6M15 6.5a3 3 0 0 1 2.5 2.5"/></svg>
    </div>
    <span>800-555-01234</span>
  </div>

  <form class="signup">
    <h2>Sign up with</h2>
    <div class="social-login"><span class="left">Linkspace</span><span class="right">Postwave</span></div>
    <div class="or"><i></i>or<i></i></div>
    <h3>Create an account</h3>
    <div class="fields">
      <div class="field">First Name</div>
      <div class="field">Last Name</div>
      <div class="field">Company</div>
      <div class="field">Select<span class="caret"><svg width="10" height="8" viewBox="0 0 10 8"><path d="M0 0h10L5 8z" fill="#777"/></svg></span></div>
      <div class="field full">Email</div>
    </div>
    <div class="btn">Sign Up</div>
    <p class="member">Already a member? <b>Login here</b></p>
  </form>
</section>

<div class="strip" role="img" aria-label="Banner illustration of a crowd of blue heads"></div>

<section class="tracks" id="products">
  <article class="track" style="left:195px">
    <div class="tab"><svg width="186" height="50" viewBox="0 0 186 50"><path d="M0 0h160l26 34H0z" fill="#4a4a4a"/><path d="M0 34h20v16z" fill="#2a2a2a"/></svg><span>Track1</span></div>
    <div class="body">
      <h4>Update, enhance or addpend you existing prospect database</h4>
      <p>Give us your ideal target title, COMPANY Size and Industry</p>
      <p>We provide contact lists derived from real-time data for your target including emails and phone numbers</p>
      <p>Coming soon: Discover what services and technologies are being evaluated or used within your lists</p>
    </div>
  </article>
  <article class="track" style="left:641px">
    <div class="tab"><svg width="186" height="50" viewBox="0 0 186 50"><path d="M0 0h160l26 34H0z" fill="#4a4a4a"/><path d="M0 34h20v16z" fill="#2a2a2a"/></svg><span>Track2</span></div>
    <div class="body">
      <h4>Update, enhance or addpend you existing prospect database</h4>
      <p>Give us your ideal target title, COMPANY Size and Industry</p>
      <p>We provide contact lists derived from real-time data for your target including emails and phone numbers</p>
      <p>Coming soon: Discover what services and technologies are being evaluated or used within your lists</p>
    </div>
  </article>
</section>

<section class="model" id="model">
  <h2 class="section-title" style="top:1168px">Unique Model</h2>
  <p class="model-sub">Lorem ipsum dolor sit amet, consectetuer adipiscing elit</p>
  <div class="diamond" style="left:181px;top:1377px"><div class="inner"><h5>Heading</h5><p>Lorem ipsum dolor sit amet, consectetuer adipiscing elit, sed diam nonummy nibh euismod tincidunt ut laoreet</p></div></div>
  <div class="diamond" style="left:490px;top:1377px"><div class="inner"><h5>Heading</h5><p>Lorem ipsum dolor sit amet, consectetuer adipiscing elit, sed diam nonummy nibh euismod tincidunt ut laoreet</p></div></div>
  <div class="diamond" style="left:799px;top:1377px"><div class="inner"><h5>Heading</h5><p>Lorem ipsum dolor sit amet, consectetuer adipiscing elit, sed diam nonummy nibh euismod tincidunt ut laoreet</p></div></div>
  <div class="diamond" style="left:335px;top:1524px"><div class="inner"><h5>Heading</h5><p>Lorem ipsum dolor sit amet, consectetuer adipiscing elit, sed diam nonummy nibh euismod tincidunt ut laoreet</p></div></div>
  <div class="diamond active" style="left:644px;top:1524px"><div class="inner"><h5>Heading</h5><p>Lorem ipsum dolor sit amet, consectetuer adipiscing elit, sed diam nonummy nibh euismod tincidunt ut laoreet</p></div></div>
</section>

<section class="pricing" id="pricing">
  <h2 class="section-title">Pricing</h2>
  <div class="plan" style="left:177px;top:130px;width:274px;height:499px">
    <div class="label" style="height:38px">BASIC</div>
    <div class="price" style="height:140px;padding-top:26px"><b>$250</b><small>PER MONTH</small></div>
    <ul><li>Lorem ipsum dolor sit amet, consecte</li><li>Lorem ipsum dolor sit amet</li><li>Lorem ipsum dolor sit amet, consecte</li><li>Lorem ipsum dolor sit amet, consecte</li><li>Lorem ipsum dolor sit amet, consecte</li><li>Lorem ipsum dolor sit amet, consecte</li></ul>
    <div class="cta" style="height:46px">GET STARTED</div>
  </div>
  <div class="plan" style="left:751px;top:130px;width:273px;height:499px">
    <div class="label" style="height:38px">ADVANCED</div>
    <div class="price" style="height:140px;padding-top:26px"><b>$750</b><small>PER YEAR</small></div>
    <ul><li>Lorem ipsum dolor sit amet, consecte</li><li>Lorem ipsum dolor sit amet</li><li>Lorem ipsum dolor sit amet, consecte</li><li>Lorem ipsum dolor sit amet, consecte</li><li>Lorem ipsum dolor sit amet, consecte</li><li>Lorem ipsum dolor sit amet, consecte</li></ul>
    <div class="cta" style="height:46px">GET STARTED</div>
  </div>
  <div class="plan" style="left:451px;top:112px;width:302px;height:535px;z-index:2">
    <div class="label" style="height:46px">STANDARD</div>
    <div class="price" style="height:150px;padding-top:24px"><b>$550</b><small>PER MONTH</small></div>
    <ul><li>Lorem ipsum dolor sit amet, consecte</li><li>Lorem ipsum dolor sit amet</li><li>Lorem ipsum dolor sit amet, consecte</li><li>Lorem ipsum dolor sit amet, consecte</li><li>Lorem ipsum dolor sit amet, consecte</li><li>Lorem ipsum dolor sit amet, consecte</li></ul>
    <div class="cta" style="height:56px">GET STARTED</div>
  </div>
</section>

<section class="about" id="about">
  <h2>About Us</h2>
  <p class="lead">Lorem ipsum dolor sit amet, consectetuer adipiscing elit, sed diam</p>
  <p class="text">Lorem ipsum dolor sit amet, consectetuer adipiscing elit, sed diam nonummy nibh euismod tincidunt ut laoreet dolore magna aliquam erat volutpat. Ut wisi enim ad minim veniam, quis nostrud exerci tation ullamcorper suscipit lobortis nisl ut aliquip ex ea commodo consequat. Duis autem vel eum iriure dolor in hendrerit in vulputate velit esse molestie consequat, vel illum dolore eu feugiat nulla facilisis at vero eros et accumsan et iusto odio dignissim qui blandit</p>
  <div class="photo" role="img" aria-label="Photograph of a smiling business team of four in suits"></div>
  <div class="btn-read">Read More</div>
</section>

<section class="contact" id="contact">
  <h2>Contact Us</h2>
  <p class="sub">Lorem ipsum dolor sit amet, consectetuer adipiscing elit</p>
  <div class="cfield" style="top:167px">Name<svg width="14" height="14" viewBox="0 0 14 14" fill="#555"><circle cx="7" cy="4" r="3"/><path d="M1 14a6 6 0 0 1 12 0z"/></svg></div>
  <div class="cfield" style="top:211px">Email<svg width="14" height="12" viewBox="0 0 14 12" fill="none" stroke="#555" stroke-width="1.4"><rect x="1" y="1" width="12" height="10"/><path d="M1 1l6 5 6-5"/></svg></div>
  <div class="cfield" style="top:256px">Phone<svg width="14" height="14" viewBox="0 0 24 24" fill="#555"><path d="M5 3h4l2 5-2.5 1.5a11 11 0 0 0 6 6L16 13l5 2v4a2 2 0 0 1-2 2A16 16 0 0 1 3 5a2 2 0 0 1 2-2z"/></svg></div>
  <div class="cmsg">Message<svg width="14" height="14" viewBox="0 0 14 14" fill="none" stroke="#555" stroke-width="1.4"><path d="M2 12l2-5 6-6 3 3-6 6z"/></svg></div>
  <div class="btn-submit">Submit</div>
</section>

<section class="callbar">
  <svg class="abs" style="left:205px;top:22px" width="52" height="52" viewBox="0 0 52 52" fill="#fff"><path d="M4 18c0-8 44-8 44 0v5h-12v-5c-6-2-14-2-20 0v5H4z"/><path d="M14 24h24l6 22H8z"/><circle cx="26" cy="34" r="6" fill="#2f3039"/></svg>
  <span class="msg">Contact us today for free consultation</span>
  <span class="num">(800-555-0187)</span>
</section>

<section class="touch">
  <h2>Get in Touch</h2>
  <p>Lorem ipsum dolor sit amet, consectetuer adipiscing elit. Aenean commodo ligula eget dolor. Aenean massa.<br>Cum sociis natoque penatibus et magnis dis parturient montes.</p>
  <div class="social-row">
    <span class="dot"></span><span class="line"></span>
    <span class="dot"></span><span class="line"></span>
    <span class="dot"></span><span class="line"></span>
    <span class="dot"></span><span class="line"></span>
    <span class="dot"></span>
  </div>
</section>

<footer class="copyright">Copyright © 2016. All rights reserved.</footer>

</body>
</html>
```